Lawn sign for construction company

Would like this to be a very clean and high end design for luxury homes. We need a yard sign designed that includes the company logo, website, phone number and major service offerings (residential and commercial renovations and maintenance)
The company website is brambleworks.com all other contact info is in the attachments
Target Market(s)
Luxury home owners and business owners
Industry/Entity Type
Construction/Home Improvement
Font styles to use
Other font styles liked:
- See company logo and other graphics included for title text fonts. All other fonts can be standard sans serif.
Colors
0054AA
0677BA
7BADD7
CADEEF
E8F1F8
Requirements
Must have
- Clean, easy to read design, would like 2 sided sign. A main sign side and back side which states “free estimates, and includes the website and phone number. Must also match the color scheme of the provided logo and other company images. Dark Navy blue primary color, gray secondary color, and orange as an accent color.
Nice to have
- 2nd sign side very simple design
Should not have
- Too many graphics limit to 1-3 colors

```html
<!DOCTYPE html>
<html lang="en">
<head>
<meta charset="utf-8">
<title>Bramble Works Company – Yard Signs</title>
<link href="https://fonts.googleapis.com/css2?family=Roboto:wght@400;500;700;900&family=Roboto+Condensed:wght@700&display=swap" rel="stylesheet">
<style>
  :root {
    --navy: #1d1a5c;
    --navy-deep: #171452;
    --orange: #c9702a;
    --grey: #767676;
    --silver: #b4b4bc;
    --white: #ffffff;
    --page: #eceef1;
  }
  * { box-sizing: border-box; margin: 0; padding: 0; }
  html, body { width: 815px; height: 1200px; overflow: hidden; }
  body {
    background: var(--page);
    font-family: "Roboto", Arial, sans-serif;
    position: relative;
  }
  .sign {
    position: absolute;
    left: 47px;
    width: 720px;
    box-shadow: 0 6px 18px rgba(0,0,0,.18);
  }
  .sign--front { top: 50px; height: 480px; background: var(--navy-deep); }
  .sign--back { top: 620px; height: 520px; background: var(--white); }

  .frame { position: absolute; }
  .sign--front .frame--outer { inset: 22px; border: 3px solid var(--silver); }
  .sign--front .frame--inner { inset: 32px; border: 1px solid var(--silver); }
  .sign--back .frame--outer { top: 22px; left: 22px; right: 22px; bottom: 88px; border: 4px solid var(--navy); border-bottom: none; }
  .sign--back .frame--inner { top: 34px; left: 34px; right: 34px; bottom: 88px; border: 1.5px solid var(--navy); border-bottom: none; }

  .brand {
    position: absolute; left: 0; right: 0;
    display: flex; align-items: center; justify-content: center; gap: 14px;
  }
  .brand__mark { border-radius: 50%; background: var(--grey); flex: none; }
  .brand__name {
    font-weight: 900; color: var(--orange);
    text-transform: uppercase; letter-spacing: .5px; line-height: 1;
  }
  .sign--front .brand { top: 170px; }
  .sign--front .brand__mark { width: 58px; height: 58px; }
  .sign--front .brand__name { font-size: 40px; }
  .sign--back .brand { top: 108px; }
  .sign--back .brand__mark { width: 44px; height: 44px; }
  .sign--back .brand__name { font-size: 30px; }

  .divider {
    position: absolute; top: 350px; left: 110px; right: 110px; height: 2px;
    background: linear-gradient(90deg, transparent, var(--silver) 15%, var(--silver) 85%, transparent);
  }
  .contact-row {
    position: absolute; top: 384px; left: 0; right: 0;
    display: flex; align-items: center; justify-content: center; gap: 18px;
    color: var(--white); font-size: 22px; letter-spacing: .5px;
  }
  .contact-row__item { display: flex; align-items: center; gap: 12px; }
  .contact-row__sep { width: 1px; height: 28px; background: var(--white); }

  .phone-line {
    position: absolute; top: 220px; left: 0; right: 0;
    display: flex; align-items: center; justify-content: center; gap: 26px;
  }
  .phone-line__icon {
    width: 62px; height: 62px; border-radius: 50%; background: var(--orange);
    display: flex; align-items: center; justify-content: center;
  }
  .phone-line__number {
    font-size: 74px; font-weight: 700; color: var(--navy); letter-spacing: 1px; line-height: 1;
  }
  .services {
    position: absolute; top: 332px; left: 0; right: 0; text-align: center;
    font-family: "Roboto Condensed", Arial, sans-serif; font-weight: 700;
    font-size: 21px; color: var(--orange); text-transform: uppercase; word-spacing: 2px;
  }
  .services__sep { margin: 0 10px; }
  .web-band {
    position: absolute; left: 0; right: 0; bottom: 18px; height: 70px;
    background: var(--navy);
    display: flex; align-items: center; justify-content: center;
    color: var(--white); font-size: 22px; font-weight: 700;
  }
</style>
</head>
<body>

<section class="sign sign--front" aria-label="Front side of yard sign">
  <div class="frame frame--outer"></div>
  <div class="frame frame--inner"></div>
  <div class="brand">
    <span class="brand__mark"></span>
    <span class="brand__name">Bramble Works Company</span>
  </div>
  <div class="divider"></div>
  <div class="contact-row">
    <span class="contact-row__item">
      <svg width="26" height="26" viewBox="0 0 24 24" aria-hidden="true">
        <circle cx="12" cy="12" r="12" fill="#fff"/>
        <path d="M8.2 5.5l2 2.6-1.1 1.6c.8 1.7 2.1 3 3.8 3.8l1.6-1.1 2.6 2-1.2 2.2c-4.6-.4-8.4-4.2-8.8-8.8z" fill="#171452"/>
      </svg>
      555-201-7384
    </span>
    <span class="contact-row__sep"></span>
    <span class="contact-row__item">
      <svg width="26" height="26" viewBox="0 0 24 24" fill="none" stroke="#fff" stroke-width="1.6" aria-hidden="true">
        <circle cx="12" cy="12" r="10"/>
        <ellipse cx="12" cy="12" rx="4.5" ry="10"/>
        <line x1="2" y1="12" x2="22" y2="12"/>
        <line x1="4" y1="7" x2="20" y2="7"/>
        <line x1="4" y1="17" x2="20" y2="17"/>
      </svg>
      brambleworks.com
    </span>
  </div>
</section>

<section class="sign sign--back" aria-label="Back side of yard sign">
  <div class="frame frame--outer"></div>
  <div class="frame frame--inner"></div>
  <div class="brand">
    <span class="brand__mark"></span>
    <span class="brand__name">Bramble Works Company</span>
  </div>
  <div class="phone-line">
    <span class="phone-line__icon">
      <svg width="34" height="34" viewBox="0 0 24 24" aria-hidden="true">
        <path d="M6.5 3l3 3.8-1.6 2.3c1.2 2.5 3.2 4.5 5.7 5.7l2.3-1.6 3.8 3-1.8 3.2C11 18.8 5.2 13 4.6 6.1z" fill="#fff"/>
      </svg>
    </span>
    <span class="phone-line__number">555-201-7384</span>
  </div>
  <p class="services">
    Residential<span class="services__sep">|</span>Commercial Renovations<span class="services__sep">|</span>Maintenance
  </p>
  <div class="web-band">brambleworks.com</div>
</section>

</body>
</html>
```